Sophisticated, clean website reflecting my feminine, playful side to sell my abstract art,

I need a website no more than 3 pages to showcase my paintings, a little about me and some contact info. I do abstracts so looking for something a little edgy, yet feminine and current.
Updates

Hi there, These are some artists websites that I Iike: Mirabelvoss.com (I like how airy it is) tobiasmerrowind.com kevinplodderas.com (I like how it scrolls) I'll need a place for a photo ( a headshot-i do not have it yet so I'll need to be able to upload that later) as well as an area for my bio. Also, it's important that I will be able to upload any new photos and descriptions easily so it should be user friendly. Lastly, I like in a sunny place so would like to have this seem upbeat and playful as that is how i like to paint. thanks-I'm trying to upload my photos now -

Target Market(s)

ppl ages 35-70 who want large scale art for their homes

Industry/Entity Type

art

Coding

Coded - Design and coding required

Number of Pages Required

3 page

Colors

Designer to choose colors to be used in the design.

Requirements
Must have
• photos of my art, a place for my bio, be easy to reach me. tasteful-nothing too "in your face" -my clients are pretty high end and organized. They like clean lines
Nice to have
• sophisticated background, muted tones in the back-similar clean font throughout-no cursive
Should not have
• too many dark areas. Too many blocks of color. Too serious.

```html
<!DOCTYPE html>
<html lang="en">
<head>
<meta charset="utf-8">
<title>Contact · Helena Marchetti Art</title>
<link rel="stylesheet" href="https://fonts.googleapis.com/css2?family=Playfair+Display:wght@600&family=Poppins:wght@400;500;600&family=Tinos&display=swap">
<style>
  :root {
    --ink: #111111;
    --text: #3a3a3a;
    --nav: #555555;
    --rule: #cfcfcf;
    --field-border: #bdbdbd;
    --accent: #318fc6;
    --footer-bg: #f8f8f8;
    --white: #ffffff;
  }
  * { box-sizing: border-box; margin: 0; padding: 0; }
  html, body { width: 1200px; height: 884px; overflow: hidden; background: var(--white); }
  body { position: relative; font-family: "Poppins", sans-serif; color: var(--text); }

  .site-title {
    position: absolute; top: 14px; left: 0; width: 1200px; text-align: center;
    font-family: "Playfair Display", serif; font-weight: 600; font-size: 36px;
    color: var(--ink); line-height: 42px;
  }
  .header-rule { position: absolute; top: 66px; left: 0; width: 1200px; height: 1px; background: var(--rule); }

  .main-nav a {
    position: absolute; top: 86px; font-size: 16.5px; line-height: 22px;
    color: var(--nav); text-decoration: none; letter-spacing: 0.2px;
  }
  .main-nav a.is-active { color: var(--ink); font-weight: 500; }

  .page-heading {
    position: absolute; top: 166px; left: 98px; font-size: 30px; font-weight: 400;
    color: var(--ink); line-height: 38px;
  }

  .field-label { position: absolute; font-size: 14px; line-height: 18px; color: var(--text); }
  .field-input {
    position: absolute; border: 1px solid var(--field-border); background: var(--white);
    font-family: inherit;
  }
  textarea.field-input { resize: none; }

  .captcha-box {
    position: absolute; left: 436px; top: 614px; width: 188px; height: 47px;
    background: #f9f9f9; border: 1px solid #d3d3d3; border-radius: 3px;
    box-shadow: 0 0 3px rgba(0,0,0,0.08);
  }
  .captcha-check {
    position: absolute; left: 8px; top: 14px; width: 17px; height: 17px;
    border: 2px solid #c1c1c1; border-radius: 2px; background: var(--white);
  }
  .captcha-text { position: absolute; left: 33px; top: 16px; font-size: 8.5px; color: #222; font-family: "Roboto", Arial, sans-serif; }
  .captcha-mark { position: absolute; left: 153px; top: 7px; width: 18px; height: 18px; border-radius: 50%; background: #b7c4d6; }
  .captcha-brand { position: absolute; right: 7px; top: 28px; font-size: 6px; color: #555; text-align: center; line-height: 7px; font-family: Arial, sans-serif; }

  .submit-button {
    position: absolute; left: 641px; top: 614px; width: 130px; height: 46px;
    background: var(--accent); color: var(--white); border: none;
    font-family: "Poppins", sans-serif; font-weight: 600; font-size: 15px; letter-spacing: 0.3px;
  }

  .site-footer { position: absolute; left: 0; top: 736px; width: 1200px; height: 148px; background: var(--footer-bg); }
  .social-link {
    position: absolute; top: 41px; width: 38px; height: 38px; border: 1.5px solid var(--ink);
    border-radius: 50%; display: flex; align-items: center; justify-content: center;
    font-size: 7.5px; color: var(--ink); text-decoration: none;
  }
  .copyright {
    position: absolute; top: 100px; left: 0; width: 1200px; text-align: center;
    font-family: "Tinos", serif; font-size: 15px; color: var(--ink);
  }
</style>
</head>
<body>
  <header>
    <h1 class="site-title">Helena Marchetti Art</h1>
    <div class="header-rule"></div>
    <nav class="main-nav">
      <a href="#" class="is-active" style="left:289px">HOME</a>
      <a href="#" style="left:435px">ABOUT ME</a>
      <a href="#" style="left:616px">MY PAINTINGS</a>
      <a href="#" style="left:830px">CONTACT</a>
    </nav>
  </header>

  <main>
    <h2 class="page-heading">Contact</h2>
    <form class="contact-form">
      <label class="field-label" style="left:99px;top:222px">First Name*</label>
      <input class="field-input" type="text" style="left:100px;top:256px;width:481px;height:48px">
      <label class="field-label" style="left:598px;top:222px">Last Name*</label>
      <input class="field-input" type="text" style="left:599px;top:256px;width:481px;height:48px">

      <label class="field-label" style="left:99px;top:328px">Email Address*</label>
      <input class="field-input" type="email" style="left:100px;top:362px;width:481px;height:48px">
      <label class="field-label" style="left:598px;top:328px">Phone Number*</label>
      <input class="field-input" type="tel" style="left:599px;top:362px;width:481px;height:48px">

      <label class="field-label" style="left:99px;top:433px">Message*</label>
      <textarea class="field-input" style="left:100px;top:466px;width:981px;height:113px"></textarea>

      <div class="captcha-box">
        <span class="captcha-check"></span>
        <span class="captcha-text">I'm not a robot</span>
        <span class="captcha-mark"></span>
        <span class="captcha-brand">VerifyBox<br>Privacy · Terms</span>
      </div>
      <button class="submit-button" type="button">SUBMIT</button>
    </form>
  </main>

  <footer class="site-footer">
    <a href="#" class="social-link" style="left:537px">Folio</a>
    <a href="#" class="social-link" style="left:580px">Chirp</a>
    <a href="#" class="social-link" style="left:625px">Lens</a>
    <p class="copyright">©Copyright ©2022 Helena Marchetti Art. All Rights Reserved.</p>
  </footer>
</body>
</html>
```